Multi App design - layout and graphic suggestions to our new app

Update:
Making a modern and futuristic design of a multifunctional app.
Attached is a description of some of the functionalities.
We need this innovative elegant design on buttons, menu, screens and other elements to be applied onto several mobile screens to choose a style that can be chosen.
Future apps will even include robot assistance, new navigation logic and 3Dish style and several templates to variate the style (look and feel).
Looking forward to see some really new style of futuristic apps!
(We like the app vrolp.com - although our design shall be even more modern and creative)

Multi-function app

We would like to have a design suggestion for a multi-function app.

The design shall show front end design as well as navigation and UI/UX user interface

It’s and generic shopping app enabling a long list of services where end user get a menu which is graphical and can be extended with new services as well as customized by end user.
Each service contains functionality as well as content and findings.
Among 5-10 initial services are:

• Shopping assistant and Travel assistant – finding relevant shops/museum and products nearby – sorted by Geofence and Beacons for presenting information - or find stores and experiences
• Loyalty points / Contests and bonus points - preferences and sharing reviews 
• QR and Barcode reader – for increased information
• Campaigns
• Support and feedback

Flexible application - with simple possibility to add new services and allow the user to control the order of the menu / own top menu
Simpler social sharing - reviews, feedback, loyalty points across shops etc.
Easy user management - turn off shops or functionality - without uninstalling

Target Market(s)

End user

Industry/Entity Type

Inn

Requirements
Must have
• The design shall show front end design as well as navigation and UI/UX user interface.
• Attached is your logo and colors with codes

```html
<!DOCTYPE html>
<html lang="en">
<head>
<meta charset="utf-8">
<title>Nearly – Home</title>
<link href="https://fonts.googleapis.com/css2?family=Lato:wght@300;400;700;900&display=swap" rel="stylesheet">
<style>
  :root {
    --teal: #0e9598;
    --orange: #ff6a00;
    --bg: #f2f2f2;
    --card: #ffffff;
    --ink: #1d1d1d;
    --ink-soft: #333c40;
    --muted: #6e6e6e;
    --tab-ink: #6a6a6a;
  }
  * { box-sizing: border-box; margin: 0; padding: 0; }
  html, body { width: 675px; height: 1200px; overflow: hidden; background: var(--bg); }
  body { font-family: "Lato", sans-serif; color: var(--ink); }
  .screen { position: relative; width: 675px; height: 1200px; overflow: hidden; background: var(--bg); }

  .app-header { position: absolute; left: 0; top: 0; width: 675px; height: 115px; background: var(--teal); color: #fff; }
  .status-bar { position: absolute; left: 0; top: 0; width: 100%; height: 40px; font-size: 19px; }
  .status-left { position: absolute; left: 10px; top: 9px; display: flex; align-items: center; gap: 6px; }
  .signal { display: flex; gap: 3px; }
  .signal span { width: 9px; height: 9px; border-radius: 50%; background: #fff; }
  .status-time { position: absolute; left: 0; right: 0; top: 9px; text-align: center; }
  .status-right { position: absolute; right: 10px; top: 9px; display: flex; align-items: center; gap: 6px; }
  .battery { width: 44px; height: 19px; border: 2px solid #fff; border-radius: 4px; padding: 2px; position: relative; }
  .battery::after { content: ""; position: absolute; right: -5px; top: 5px; width: 3px; height: 6px; background: #fff; border-radius: 0 2px 2px 0; }
  .battery span { display: block; width: 100%; height: 100%; background: #fff; border-radius: 1px; }
  .header-title { position: absolute; left: 0; right: 0; top: 56px; text-align: center; font-size: 31px; font-weight: 700; letter-spacing: 0.5px; }
  .header-icon { position: absolute; top: 56px; }
  .header-icon.home { left: 34px; }
  .header-icon.search { right: 36px; }

  .section-title { position: absolute; left: 36px; font-size: 22px; }
  .section-title.strong { font-weight: 700; color: var(--ink); }
  .section-title.plain { color: var(--ink); }
  .section-title.soft { color: #505558; }
  .points { color: var(--orange); font-weight: 700; }

  .card-row { position: absolute; left: 0; width: 675px; height: 288px; }
  .card { position: absolute; top: 0; width: 360px; height: 288px; background: var(--card); border-radius: 3px; overflow: hidden; }
  .card-image { position: relative; height: 180px; }
  .card-name { position: absolute; left: 19px; top: 30px; font-size: 23px; color: var(--ink-soft); }
  .card-body { position: relative; height: 108px; }
  .card-meta { position: absolute; left: 19px; top: 73px; font-size: 19px; font-weight: 300; color: var(--muted); }
  .point-badge { position: absolute; left: 18px; bottom: 8px; display: flex; align-items: center; gap: 7px; color: #fff; font-weight: 700; font-size: 20px; }
  .point-badge::before { content: ""; width: 18px; height: 18px; border-radius: 50%; background: var(--orange); }

  .meal-row { position: absolute; left: 0; top: 947px; width: 675px; height: 170px; }
  .meal-tile { position: absolute; top: 0; width: 180px; height: 180px; border-radius: 3px; overflow: hidden; }
  .rating { position: absolute; left: 9px; top: 9px; width: 45px; height: 36px; background: var(--teal); color: #fff; font-size: 22px; display: flex; align-items: center; justify-content: center; border-radius: 2px; }

  .tab-bar { position: absolute; left: 0; top: 1112px; width: 675px; height: 88px; background: rgba(250,250,250,0.97); box-shadow: 0 -6px 14px rgba(0,0,0,0.06); }
  .tab { position: absolute; top: 14px; width: 120px; margin-left: -60px; text-align: center; color: var(--tab-ink); font-size: 20px; font-weight: 300; }
  .tab svg { display: block; margin: 0 auto 10px; }
</style>
</head>
<body>
<div class="screen">

  <header class="app-header">
    <div class="status-bar">
      <div class="status-left">
        <div class="signal"><span></span><span></span><span></span><span></span><span></span></div>
        <span>Carrier</span>
        <svg width="22" height="16" viewBox="0 0 22 16" fill="none" stroke="#fff" stroke-width="2.2" stroke-linecap="round"><path d="M2 5.5a13 13 0 0 1 18 0"/><path d="M5.5 9a8 8 0 0 1 11 0"/><circle cx="11" cy="13" r="1.6" fill="#fff" stroke="none"/></svg>
      </div>
      <div class="status-time">9:41 AM</div>
      <div class="status-right"><span>100%</span><div class="battery"><span></span></div></div>
    </div>
    <svg class="header-icon home" width="34" height="34" viewBox="0 0 34 34" fill="none" stroke="#fff" stroke-width="2" stroke-linejoin="round"><path d="M3 16 17 3l14 13"/><path d="M7 13v18h7v-9h6v9h7V13"/></svg>
    <div class="header-title">NEARLY</div>
    <svg class="header-icon search" width="34" height="34" viewBox="0 0 34 34" fill="none" stroke="#fff" stroke-width="2.2" stroke-linecap="round"><circle cx="14" cy="14" r="11"/><path d="M22 22l9 9"/></svg>
  </header>

  <h2 class="section-title strong" style="top:156px">6 new places you might like</h2>
  <div class="card-row" style="top:202px">
    <article class="card" style="left:36px">
      <div class="card-image" role="img" aria-label="Plated duck breast with glazed fruit and greens on a dark dish" style="background:radial-gradient(ellipse at 45% 45%, #9a5a3c 0%, #4a3028 40%, #1e1c1b 80%)"></div>
      <div class="card-body"><h3 class="card-name" style="font-weight:400">Sakura Harbour</h3><p class="card-meta">Havnegata 4, Oslo</p></div>
    </article>
    <article class="card" style="left:432px">
      <div class="card-image" role="img" aria-label="Restaurant interior with dark leather booths and wooden tables" style="background:linear-gradient(180deg, #5a4a3c 0%, #3a302a 45%, #1c1a19 100%)"></div>
      <div class="card-body"><h3 class="card-name" style="font-weight:400">Linden Table</h3><p class="card-meta">Lindeveien, Oslo</p></div>
    </article>
  </div>

  <h2 class="section-title plain" style="top:527px">You have <span class="points">1400</span> point, use it on below</h2>
  <div class="card-row" style="top:574px">
    <article class="card" style="left:36px">
      <div class="card-image" role="img" aria-label="Chefs plating dishes in a busy restaurant kitchen" style="background:linear-gradient(180deg, #6f6a62 0%, #3d3a36 55%, #1f1e1c 100%)">
        <span class="point-badge">1200 Point</span>
      </div>
      <div class="card-body"><h3 class="card-name" style="font-weight:400">Nordlys Kitchen</h3><p class="card-meta">20% Discount</p></div>
    </article>
    <article class="card" style="left:439px">
      <div class="card-image" role="img" aria-label="Steak plate and soup bowl on a newspaper-covered table" style="background:linear-gradient(120deg, #d8cfc6 0%, #b9a89a 50%, #8a5a48 100%)">
        <span class="point-badge">1320 Point</span>
      </div>
      <div class="card-body"><h3 class="card-name" style="font-weight:400">Brasserie Lumière</h3><p class="card-meta">Free dessert</p></div>
    </article>
  </div>

  <h2 class="section-title soft" style="top:901px;font-weight:400">Best meal in the city</h2>
  <div class="meal-row">
    <div class="meal-tile" style="left:36px" role="img" aria-label="Baked onion soup in a white bowl with bread" >
      <div style="position:absolute;inset:0;background:radial-gradient(circle at 45% 55%, #d99a3a 0%, #e8d2a8 35%, #f1ece4 70%)"></div>
      <span class="rating">4.2</span>
    </div>
    <div class="meal-tile" style="left:248px" role="img" aria-label="Plated dish with berries and herbs on a wooden board">
      <div style="position:absolute;inset:0;background:radial-gradient(circle at 50% 60%, #8a6a4e 0%, #3e3a34 50%, #1c1c1b 100%)"></div>
      <span class="rating">4.2</span>
    </div>
    <div class="meal-tile" style="left:459px" role="img" aria-label="Spaghetti with greens twirled on a fork in a bowl">
      <div style="position:absolute;inset:0;background:radial-gradient(circle at 50% 60%, #b5a04a 0%, #6a6a3a 40%, #2a2a26 100%)"></div>
      <span class="rating">4.2</span>
    </div>
  </div>

  <nav class="tab-bar">
    <div class="tab" style="left:68px">
      <svg width="40" height="36" viewBox="0 0 40 36" fill="none" stroke="#1d1d1d" stroke-width="2.4" stroke-linejoin="round"><path d="M3 6l11-4 12 4 11-4v28l-11 4-12-4-11 4z"/><path d="M14 2v28M26 6v28"/></svg>
      Places
    </div>
    <div class="tab" style="left:248px">
      <svg width="38" height="36" viewBox="0 0 38 36" fill="none" stroke="#1d1d1d" stroke-width="3"><path d="M2 11V2h10M26 2h10v9M36 25v9H26M12 34H2v-9"/></svg>
      Scan
    </div>
    <div class="tab" style="left:428px">
      <svg width="36" height="40" viewBox="0 0 36 40" fill="#1d1d1d"><circle cx="18" cy="13" r="12"/><circle cx="18" cy="13" r="7" fill="none" stroke="#fff" stroke-width="2"/><path d="M10 22 4 36l7-2 4 5 3-10zM26 22l6 14-7-2-4 5-3-10z"/></svg>
      Point
    </div>
    <div class="tab" style="left:616px">
      <svg width="36" height="38" viewBox="0 0 36 38" fill="#1d1d1d"><circle cx="18" cy="10" r="9"/><path d="M2 37c0-10 7-16 16-16s16 6 16 16z"/></svg>
      Profile
    </div>
  </nav>

</div>
</body>
</html>
```